Brand Business Card for Hotel Cloud Management System

Hello designers,
we are looking for a new brand business card for our product Stayvora. Our brand Stayvora is a hotel management system for small hotels, B&B, guesthouses etc. and just recently we are expanding our offer to other European markets. Therefore we need a business card that will communicate not only to the end-users (hoteliers) but also to potential business partners/ We would like the brand business card to be professional looking, but not too serius, modern, elegant, clean, Our brand color is orange, dark grey and it would be nice to see both combined.

Please visit our website www.stayvora.eu to get more impression on what our brand stayvora stands for.

Please find attached stayvora logo.

Target Market(s)

small hotels, hoteliers, B&B owners, potential business partners

Industry/Entity Type

Software Service

Contact Information for Business Card

Stayvora
- hotel software solutions - web booking engine - multi channel manager
www.stayvora.eu
T: +38614738265
E: info@stayvora.net

Font styles to use
Serif
Sans Serif

Colors
f37122
aaaaaa
606060
f6f6f6

Requirements
Must have
• Logo of the brand
• the layout of the business card should be in connection with the look and feel of the website stayvora.eu and logo stayvora;

```html
<!DOCTYPE html>
<html lang="en">
<head>
<meta charset="utf-8">
<title>Stayvora – Business Card</title>
<link rel="stylesheet" href="https://fonts.googleapis.com/css2?family=Roboto:wght@400;500;700&display=swap">
<style>
  :root {
    --orange: #e5672a;
    --orange-bright: #f37122;
    --paper: #f2f2f2;
    --ink: #1c1c1c;
    --charcoal: #1d1e20;
    --backdrop: #e4e4e4;
    --white: #ffffff;
  }
  * { box-sizing: border-box; margin: 0; padding: 0; }
  html, body { width: 1200px; height: 960px; overflow: hidden; }
  body {
    background: var(--backdrop);
    font-family: "Roboto", Arial, sans-serif;
    position: relative;
  }
  .card {
    position: absolute;
    width: 600px;
    height: 343px;
    border-radius: 20px;
    overflow: hidden;
  }
  .card-front { left: 314px; top: 113px; background: var(--paper); }
  .card-back { left: 311px; top: 472px; background: var(--charcoal); }

  .front-shape { position: absolute; inset: 0; }

  .holder { position: absolute; left: 30px; top: 88px; color: var(--white); }
  .holder-name { font-size: 22px; font-weight: 500; letter-spacing: 0.2px; line-height: 1; }
  .holder-role { font-size: 14px; font-weight: 500; margin-top: 6px; }

  .contacts { position: absolute; left: 30px; top: 196px; list-style: none; color: var(--white); font-size: 14px; }
  .contacts li { display: flex; align-items: center; height: 19px; }
  .contacts svg { width: 12px; height: 12px; margin-right: 10px; fill: var(--white); }

  .brand-front { position: absolute; left: 316px; top: 178px; width: 228px; text-align: center; }
  .brand-name {
    display: inline-flex; align-items: center; gap: 8px;
    font-size: 40px; font-weight: 700; color: var(--ink); line-height: 1; letter-spacing: -0.5px;
  }
  .brand-dot { width: 12px; height: 12px; border-radius: 50%; background: var(--orange-bright); }
  .brand-tag { font-size: 13px; color: var(--ink); margin-top: 5px; }

  .brand-back {
    position: absolute; left: 0; right: 0; top: 140px; text-align: center;
    font-size: 64px; font-weight: 700; color: var(--orange-bright); line-height: 1; letter-spacing: -1px;
  }
  .services {
    position: absolute; left: 0; right: 0; top: 294px; text-align: center;
    color: var(--white); font-size: 14px;
  }
  .services .sep {
    display: inline-block; width: 6px; height: 6px; border-radius: 50%;
    background: var(--orange-bright); margin: 0 3px; vertical-align: middle;
  }
</style>
</head>
<body>
  <section class="card card-front">
    <svg class="front-shape" viewBox="0 0 600 343" width="600" height="343" aria-hidden="true">
      <path d="M0 0 H296 Q238 170 314 343 H0 Z" fill="var(--orange)"/>
      <path d="M311 0 Q252 150 264 285 Q266 140 318 0 Z" fill="var(--orange)"/>
    </svg>

    <div class="holder">
      <p class="holder-name">MARTA KOVAC</p>
      <p class="holder-role">CEO/FOUNDER</p>
    </div>

    <ul class="contacts">
      <li>
        <svg viewBox="0 0 24 24"><path d="M6.6 10.8a15.2 15.2 0 0 0 6.6 6.6l2.2-2.2c.3-.3.7-.4 1-.2 1.1.4 2.3.6 3.6.6.6 0 1 .4 1 1V20c0 .6-.4 1-1 1A17 17 0 0 1 3 4c0-.6.4-1 1-1h3.5c.6 0 1 .4 1 1 0 1.3.2 2.5.6 3.6.1.3 0 .7-.2 1z"/></svg>
        +38614738265
      </li>
      <li>
        <svg viewBox="0 0 24 24"><path d="M2 5h20v14H2z M3 6l9 7 9-7" fill="none" stroke="#fff" stroke-width="2"/></svg>
        info@stayvora.net
      </li>
      <li>
        <svg viewBox="0 0 24 24"><circle cx="12" cy="12" r="10"/><path d="M7 8c2 0 3 1 3 3s2 1 2 3-1 3-1 5M15 5c-1 2 1 3 3 3" stroke="var(--orange)" stroke-width="2" fill="none"/></svg>
        www.stayvora.eu
      </li>
    </ul>

    <div class="brand-front">
      <p class="brand-name"><span class="brand-dot"></span>Stayvora</p>
      <p class="brand-tag">hotel pms service</p>
    </div>
  </section>

  <section class="card card-back">
    <p class="brand-back">Stayvora</p>
    <p class="services">hotel software solutions<span class="sep"></span>web booking engine<span class="sep"></span>multi channel manager</p>
  </section>
</body>
</html>
```